Upmarket cover for top management book, ideally unlike most common cover pages

This book is about both good management and mismanagement and introduces novel concepts such as the inverse exponential law in strategy, No doubt that these concepts will be criticized by some management scholars. However, students, a few other colleagues and key top managers find the new ideas useful and eye-opening.
The cover must help communicate a deeper vision of management as an expression of life creation and a sort of "divine" energy.

Practical details:
Print and ebook cover page plus elements of the cover for each of the three main book sections.
Title; The Harbor
Subtitle: Field methods and the quiet ripple rule
Author: Teodor M. Vasquel
Publisher: Brightwell Page Press
Width x height: 13,97 x 21,59 cm (without bleed)
Spine: 14-15 cm according to paper color

Target Market(s)

Mostly managers who did not have the opportunity of attending postgraduate management studies such as the MBA

Industry/Entity Type

Mostly high technology

Font styles to use
Serif
Sans Serif
Other font styles liked:
• Arial nova, Arial light

Requirements
Must have
• Preferably cover and back cover on white background, but any good proposals would do.
Nice to have
• An image of bright and reassuring, albeit potentially unlimited, strength. Ideally the cover design should show that good management is good for the COMMON GOOD of society
Should not have
• Please do not show images of people and no proposals reminiscent of other management and strategy book covers

```html
<!DOCTYPE html>
<html lang="en">
<head>
<meta charset="utf-8">
<title>The Harbor — Teodor M. Vasquel</title>
<link href="https://fonts.googleapis.com/css2?family=Bebas+Neue&family=Oswald:wght@300;400;600&display=swap" rel="stylesheet">
<style>
  :root {
    --ink-dark: #1f1b18;
    --ink-mid: #2c2622;
    --board-dark: #0f0e0d;
    --gold-deep: #b9863a;
    --gold-mid: #d9ae4a;
    --gold-bright: #fde868;
    --paper: #ffffff;
  }
  html, body {
    margin: 0;
    padding: 0;
    overflow: hidden;
    background: var(--ink-dark);
  }
  .cover {
    position: relative;
    width: 800px;
    height: 1200px;
    overflow: hidden;
    background: linear-gradient(180deg, var(--ink-dark) 0%, var(--ink-dark) 45%, var(--ink-mid) 72%, var(--board-dark) 100%);
  }
  .cover-art {
    position: absolute;
    left: 0;
    top: 500px;
    width: 800px;
    height: 700px;
    background:
      radial-gradient(ellipse 120px 300px at 400px 330px, rgba(201,160,80,0.85) 0%, rgba(150,110,50,0.55) 55%, rgba(60,45,30,0) 100%),
      radial-gradient(ellipse 180px 50px at 400px 560px, rgba(190,150,70,0.6) 0%, rgba(40,32,26,0) 100%),
      linear-gradient(180deg, rgba(0,0,0,0) 0%, rgba(0,0,0,0) 55%, rgba(20,18,17,0.9) 75%, var(--board-dark) 100%);
  }
  .cover-type {
    position: absolute;
    inset: 0;
  }
  .title-small,
  .title-large {
    font-family: "Bebas Neue", "Oswald", sans-serif;
  }
  .subtitle {
    font-family: "Oswald", sans-serif;
    font-weight: 400;
    fill: var(--paper);
  }
  .author {
    font-family: "Oswald", sans-serif;
    font-weight: 600;
    fill: var(--paper);
  }
</style>
</head>
<body>
  <main class="cover">
    <div class="cover-art" role="img" aria-label="Photograph of a polished gold chess king standing on a dark chessboard against a dark background"></div>

    <svg class="cover-type" width="800" height="1200" viewBox="0 0 800 1200" xmlns="http://www.w3.org/2000/svg">
      <defs>
        <linearGradient id="goldFoil" x1="66" y1="0" x2="734" y2="0" gradientUnits="userSpaceOnUse">
          <stop offset="0" stop-color="var(--gold-deep)"/>
          <stop offset="0.3" stop-color="var(--gold-mid)"/>
          <stop offset="0.55" stop-color="var(--gold-bright)"/>
          <stop offset="0.8" stop-color="var(--gold-mid)"/>
          <stop offset="1" stop-color="var(--gold-deep)"/>
        </linearGradient>
      </defs>

      <text class="title-small" x="400" y="196" text-anchor="middle" font-size="108" fill="url(#goldFoil)">THE</text>
      <text class="title-large" x="66" y="380" font-size="218" fill="url(#goldFoil)" textLength="668" lengthAdjust="spacingAndGlyphs">HARBOR</text>

      <text class="subtitle" x="80" y="440" font-size="34" textLength="641" lengthAdjust="spacing">FIELD METHODS AND THE QUIET RIPPLE RULE</text>

      <text class="author" x="400" y="1141" font-size="56" text-anchor="middle" textLength="560" lengthAdjust="spacing">TEODOR M. VASQUEL</text>
    </svg>
  </main>
</body>
</html>
```